Trivia Game

I need a website designed for a Wordpress site. The site will be a contest site that will allow players to compete in trivia contests for money, including crypto currencies.

Target Market(s)

people who want to play trivia games for cash

Industry/Entity Type

Games

Number of Pages Required

1 page

Colors

Designer to choose colors to be used in the design.

Requirements
Must have
• A place for a video. A call to action - Signup.
• Black and gold like a casino.
• Very classy
Nice to have
• attached are some examples of the style I want. Very sparkly, clean classy, like a casino.

```html
<!DOCTYPE html>
<html lang="en">
<head>
<meta charset="utf-8">
<title>Vanto – Trivia Game</title>
<link href="https://fonts.googleapis.com/css2?family=Montserrat:wght@400;500;600&family=Open+Sans:wght@700;800&family=PT+Sans:wght@400;700&display=swap" rel="stylesheet">
<style>
  :root{
    --gold:#c98a0c;
    --gold-bright:#d9960f;
    --cyan:#0cb4d9;
    --black:#000;
    --panel:#262626;
    --header:#1e1e1e;
    --tile:#333333;
    --cta:#3a3a3a;
    --footer:#232323;
    --white:#fff;
    --muted:#c9c9c9;
    --text-dark:#333;
  }
  *{margin:0;padding:0;box-sizing:border-box}
  html,body{width:1200px;height:2727px;overflow:hidden;background:var(--black)}
  body{position:relative;font-family:"PT Sans",sans-serif;color:var(--white)}

  /* header */
  .site-header{position:absolute;left:0;top:0;width:1200px;height:74px;background:var(--header)}
  .brand{position:absolute;font-family:"PT Sans",sans-serif;font-weight:700;color:var(--gold)}
  .header-brand{left:131px;top:12px;font-size:40px;line-height:48px}
  .nav{position:absolute;left:545px;top:22px;width:530px;height:30px;font-family:"Montserrat",sans-serif;font-size:11px;font-weight:500;letter-spacing:.3px}
  .nav a{position:absolute;top:0;color:var(--white);text-decoration:none;line-height:30px;white-space:nowrap}
  .nav a.active{left:0;width:66px;text-align:center;border:1px solid var(--gold);color:var(--gold-bright);line-height:28px}
  .nav a.signup{left:444px;width:78px;top:1px;text-align:center;background:var(--gold);line-height:28px}

  /* hero */
  .hero{position:absolute;left:0;top:74px;width:1200px;height:562px;background:var(--cyan)}
  .hero-title{position:absolute;left:164px;top:152px;font-size:41px;font-weight:700;line-height:1}
  .hero-text{position:absolute;left:164px;top:212px;width:270px;font-size:13px;line-height:17px}
  .btn-light{position:absolute;left:164px;top:300px;width:123px;height:37px;background:var(--white);color:var(--cyan);font-family:"Montserrat",sans-serif;font-weight:600;font-size:13px;line-height:37px;text-align:center;letter-spacing:.5px}
  .hero-art{position:absolute;left:545px;top:72px;width:475px;height:470px;border-radius:14px;
    background:linear-gradient(180deg,#f5c21b 0%,#1fc7b0 22%,#e8234a 38%,#1b2e4a 52%,#e9eef7 70%,#f06a2a 80%,#1b2e4a 100%)}

  /* how it works */
  .how-bg{position:absolute;left:0;top:636px}
  .section-title{position:absolute;font-family:"Open Sans",sans-serif;font-weight:800;color:var(--gold-bright);font-size:29px;letter-spacing:.5px;line-height:1}
  .how-title{left:218px;top:686px}
  .how-text{position:absolute;left:218px;top:734px;width:700px;font-size:13px;line-height:19px;color:var(--muted)}
  .video{position:absolute;left:218px;top:795px;width:769px;height:387px;background:linear-gradient(180deg,#3cb58f 0%,#2fa982 100%)}
  .video-caption{position:absolute;left:0;bottom:4px;width:100%;text-align:center;font-size:10px;color:#d6efe6}
  .play{position:absolute;left:569px;top:948px}

  /* categories */
  .center{position:absolute;left:0;width:1200px;text-align:center}
  .cat-title{top:1307px}
  .sub{font-size:13px;color:var(--muted)}
  .cat-sub{top:1347px}
  .categories{position:absolute;left:133px;top:1409px;display:flex;gap:19px}
  .cat{width:172px;height:154px;background:var(--tile);display:flex;flex-direction:column;align-items:center;padding-top:26px;font-family:"Montserrat",sans-serif;font-weight:600;font-size:13px}
  .cat svg{width:58px;height:58px;margin-bottom:24px}
  .cat.active{background:var(--gold)}
  .arrow{position:absolute;top:1472px}

  /* top games */
  .games-title{top:1627px}
  .games{position:absolute;left:133px;top:1705px;display:flex;gap:12px}
  .game{width:226px;height:339px;background:var(--white);padding:6px;position:relative}
  .game-art{width:214px;height:212px}
  .game h3{margin:18px 0 0 14px;font-family:"Open Sans",sans-serif;font-weight:700;font-size:13px;color:var(--text-dark);letter-spacing:.2px}
  .game p{margin:4px 0 0 14px;width:180px;font-size:12px;line-height:15px;color:#555}
  .btn-play{position:absolute;left:20px;top:295px;width:64px;height:25px;background:var(--gold);font-family:"Montserrat",sans-serif;font-weight:600;font-size:12px;line-height:25px;text-align:center}

  /* cta */
  .cta{position:absolute;left:0;top:2069px;width:1200px;height:309px;background:var(--cta)}
  .cta-title{top:2174px}
  .cta-text{position:absolute;left:340px;top:2224px;width:520px;text-align:center;font-size:15px;line-height:20px}
  .btn-gold{position:absolute;left:542px;top:2294px;width:116px;height:38px;background:var(--gold);font-family:"Montserrat",sans-serif;font-weight:600;font-size:15px;line-height:38px;text-align:center}

  /* footer */
  .footer{position:absolute;left:0;top:2378px;width:1200px;height:349px;background:var(--footer)}
  .f-col{position:absolute;top:2434px;font-size:12px;color:var(--muted)}
  .f-col h4{font-family:"Montserrat",sans-serif;font-weight:600;font-size:14px;color:var(--white);letter-spacing:.5px;margin-bottom:16px}
  .f-col li{list-style:none;line-height:25.5px}
  .social li{display:flex;align-items:center;gap:14px;line-height:15px;margin-bottom:16px;font-size:11px;color:var(--white)}
  .social .dot{width:26px;height:26px;border-radius:50%;flex:none}
  .footer-brand{left:849px;top:2426px;font-size:60px;line-height:70px}
  .f-about{position:absolute;left:849px;top:2512px;width:220px;font-size:12px;line-height:17px;color:var(--muted)}
  .f-rule{position:absolute;left:133px;top:2640px;width:936px;height:1px;background:#555}
  .copyright{top:2678px;font-size:12px}
</style>
</head>
<body>

<header class="site-header">
  <div class="brand header-brand">Vanto</div>
  <nav class="nav">
    <a class="active">HOME</a><a style="left:91px">ABOUT US</a><a style="left:188px">GAMES</a><a style="left:268px">BLOG</a><a style="left:331px">CONTACT US</a><a class="signup">SIGNUP</a>
  </nav>
</header>

<section class="hero">
  <h1 class="hero-title">Trivia Game</h1>
  <p class="hero-text">There are many variations of passages of Lorem Ipsum available, but the majority have suffered.</p>
  <div class="btn-light">READ MORE</div>
  <div class="hero-art" role="img" aria-label="Illustration of a laptop showing a quiz screen with question, tick and exclamation speech bubbles above it"></div>
</section>

<svg class="how-bg" width="1200" height="611" viewBox="0 0 1200 611" aria-hidden="true">
  <polygon points="73,0 1127,0 1200,64 1200,554 1127,611 73,611 0,554 0,64" fill="#262626"/>
</svg>
<h2 class="section-title how-title">HOW IT WORKS</h2>
<p class="how-text">There are many variations of passages of Lorem Ipsum available, but the majority have suffered.by injected humour, or randomised words which don't look even slightl embarrassing hidden in the middle of text.</p>
<div class="video" role="img" aria-label="Video still: illustrated group of people with phones around large quiz speech bubbles">
  <p class="video-caption">Lorem ipsum dolor sit amet, consectetur adipiscing elit, sed do eiusmod tempor incididunt ut labore et dolore magna aliqua.</p>
</div>
<svg class="play" width="72" height="72" viewBox="0 0 72 72" aria-label="Play video">
  <circle cx="36" cy="36" r="36" fill="#e0242c"/>
  <polygon points="28,22 52,36 28,50" fill="#fff"/>
</svg>

<h2 class="section-title center cat-title">CATEGORIES</h2>
<p class="center sub cat-sub">There are many variations of passages of Lorem Ipsum available but the majority have</p>
<svg class="arrow" style="left:80px" width="16" height="28" viewBox="0 0 16 28" aria-hidden="true"><polyline points="13,3 3,14 13,25" fill="none" stroke="#fff" stroke-width="3"/></svg>
<div class="categories">
  <div class="cat">
    <svg viewBox="0 0 58 58" fill="none" stroke="#ddd" stroke-width="3"><ellipse cx="20" cy="40" rx="11" ry="10"/><circle cx="20" cy="40" r="3"/><line x1="26" y1="33" x2="46" y2="13"/><rect x="43" y="6" width="8" height="10" transform="rotate(45 47 11)"/></svg>
    POP MUSIC
  </div>
  <div class="cat">
    <svg viewBox="0 0 58 58" fill="none" stroke="#ddd" stroke-width="3"><rect x="12" y="14" width="34" height="24" rx="2"/><path d="M5 44h48l-3 4H8z"/></svg>
    COMPUTER
  </div>
  <div class="cat active">
    <svg viewBox="0 0 58 58" fill="none" stroke="#fff" stroke-width="3"><circle cx="29" cy="24" r="14"/><ellipse cx="29" cy="24" rx="6" ry="14"/><line x1="15" y1="24" x2="43" y2="24"/><path d="M12 30a18 18 0 0 0 34 0"/><line x1="29" y1="42" x2="29" y2="50"/><line x1="20" y1="51" x2="38" y2="51"/></svg>
    GEOGRAPHY
  </div>
  <div class="cat">
    <svg viewBox="0 0 58 58" fill="none" stroke="#ddd" stroke-width="3"><line x1="16" y1="8" x2="42" y2="8"/><line x1="16" y1="50" x2="42" y2="50"/><path d="M19 8c0 14 20 14 20 21s-20 7-20 21M39 8c0 14-20 14-20 21s20 7 20 21"/></svg>
    HISTORY
  </div>
  <div class="cat">
    <svg viewBox="0 0 58 58" fill="none" stroke="#ddd" stroke-width="3"><rect x="9" y="10" width="40" height="38"/><line x1="17" y1="10" x2="17" y2="48"/><line x1="41" y1="10" x2="41" y2="48"/><polygon points="25,21 35,29 25,37" fill="#ddd"/></svg>
    MOVIE
  </div>
</div>
<svg class="arrow" style="left:1100px" width="16" height="28" viewBox="0 0 16 28" aria-hidden="true"><polyline points="3,3 13,14 3,25" fill="none" stroke="#fff" stroke-width="3"/></svg>

<h2 class="section-title center games-title">TOP GAMES</h2>
<div class="games">
  <article class="game">
    <div class="game-art" role="img" aria-label="Illustration of a winner screen surrounded by game and prize icons" style="background:linear-gradient(180deg,#2ea6d8,#1b8fc4)"></div>
    <h3>LOREM IPSUM IS SIMPLY</h3>
    <p>There are many variations of passages of Lorem Ipsum.</p>
    <div class="btn-play">PLAY</div>
  </article>
  <article class="game">
    <div class="game-art" role="img" aria-label="Isometric illustration of a city rising from a tablet" style="background:linear-gradient(180deg,#2b1d2c,#3d2534)"></div>
    <h3>LOREM IPSUM IS SIMPLY</h3>
    <p>There are many variations of passages of Lorem Ipsum.</p>
    <div class="btn-play">PLAY</div>
  </article>
  <article class="game">
    <div class="game-art" role="img" aria-label="Illustration of a checklist clipboard under a magnifying glass" style="background:linear-gradient(180deg,#18b5dc,#0fa6cf)"></div>
    <h3>LOREM IPSUM IS SIMPLY</h3>
    <p>There are many variations of passages of Lorem Ipsum.</p>
    <div class="btn-play">PLAY</div>
  </article>
  <article class="game">
    <div class="game-art" role="img" aria-label="Photo of blue program code on a screen" style="background:linear-gradient(180deg,#0a2a4a,#0f3c66)"></div>
    <h3>LOREM IPSUM IS SIMPLY</h3>
    <p>There are many variations of passages of Lorem Ipsum.</p>
    <div class="btn-play">PLAY</div>
  </article>
</div>

<section class="cta"></section>
<h2 class="section-title center cta-title">READY TO PLAY GAME?</h2>
<p class="cta-text">There are many variations of passages of Lorem Ipsum available but the majority have suffered alteration in some form by injected humour</p>
<div class="btn-gold">SIGN UP</div>

<footer class="footer"></footer>
<div class="f-col" style="left:133px"><h4>ABOUT</h4><ul><li>Company</li><li>Mission</li><li>FAQ</li></ul></div>
<div class="f-col" style="left:295px"><h4>MENU</h4><ul><li>Home</li><li>Games</li><li>Blog</li><li>Contact Us</li></ul></div>
<div class="f-col" style="left:462px"><h4>TERMS &amp; POLICIES</h4><ul><li>Terms &amp; Conditions</li><li>Privacy Policy</li><li>Sitemap</li></ul></div>
<div class="f-col social" style="left:685px"><h4>FOLLOW US</h4>
  <ul>
    <li><span class="dot" style="background:#3b5998"></span><span>Follow us<br>CIRCLEBOOK</span></li>
    <li><span class="dot" style="background:#1da1f2"></span><span>Follow us<br>CHIRPER</span></li>
    <li><span class="dot" style="background:#1f3f7a"></span><span>Follow us<br>WORKLINK</span></li>
  </ul>
</div>
<div class="brand footer-brand">Vanto</div>
<p class="f-about">There are many variations of passages of Lorem Ipsum available but the majority have suffered alteration in some form by injected humour</p>
<div class="f-rule"></div>
<p class="center copyright">Copyrights @ 2018 All Rights Reserved</p>

</body>
</html>
```